Roadside building business signage for a holistic health clinic.

Replace signs as shown in the attached file. They are perforated stickers that go on the windows as shown. Looking for something that has our logo and says the name of the practice with logo (Fernbrook Health & Wellness) also boldly says Acupuncture, IV Vitamins, and Holistic Health.
Possibly our phone number as well 318-627-5194
Updates

Please don't use pink except the logo. Earthy, organic tone colors appreciated.

Need of eye catching window signage of a holistic clinic on a brick building. Pink, purple, sage green, white color. Logo is pink on a white background. Please don't overload with too much pink. Words to include are "Fernbrook Health and Wellness(name of business)", "Direct Primary Care", " Medical acupuncture", "IV Vitamin Therapy", "fernbrookcare-example.com","318-627-5194".

Target Market(s)

People will see in their cars passing by the building. Busy roadside so need to be visible while passing in fast speed.

Industry/Entity Type

Health & Wellness

Font styles to use
Sans Serif

Colors

Designer to choose colors to be used in the design.

Requirements
Must have
• On sign must have words Holistic Medicine, Medical Acupuncture, Direct Primary Care and IV vitamins.
Nice to have
• Simple, minimalistic, artistic yet has clear message. White, Black, Violet, Pink (logo), Dark green, Sage green.
Should not have
• Bold colors (red, yellow, blue), same tone colors. Blue waves on the current signage (uploaded file) must go.

```html
<!DOCTYPE html>
<html lang="en">
<head>
<meta charset="utf-8">
<title>Fernbrook Health &amp; Wellness – Window Panels</title>
<link rel="stylesheet" href="https://fonts.googleapis.com/css2?family=Raleway:wght@600;700;800&family=Oswald:wght@500&family=Roboto+Condensed:wght@700&display=swap">
<style>
  :root {
    --backdrop: #9d9d9d;
    --panel: #edebe3;
    --wave: #f8f7f3;
    --ink-green: #2f4a3b;
    --sage: #8fa58c;
    --sage-soft: #c9d5c4;
    --violet: #6b4f87;
    --logo-pink: #d91c73;
  }
  * { box-sizing: border-box; margin: 0; padding: 0; }
  html, body { width: 1200px; height: 515px; overflow: hidden; }
  body { background: var(--backdrop); position: relative; font-family: "Raleway", sans-serif; }

  .panel {
    position: absolute; width: 149px; height: 150px;
    background: var(--panel); overflow: hidden;
    display: flex; flex-direction: column; align-items: center; justify-content: center;
    text-align: center; color: var(--ink-green);
  }
  .panel--arch-left { border-top-left-radius: 100% 100%; }
  .panel--arch-right { border-top-right-radius: 100% 100%; }

  .wave-decor {
    position: absolute; top: 0; right: 0; width: 70px; height: 42px;
    background: linear-gradient(200deg, var(--wave) 0%, rgba(248,247,243,0) 75%);
  }
  .wave-decor--left { right: auto; left: 0; background: linear-gradient(160deg, var(--wave) 0%, rgba(248,247,243,0) 75%); }
  .leaf-decor {
    position: absolute; bottom: 0; width: 50px; height: 30px;
    background: linear-gradient(0deg, var(--sage-soft) 0%, rgba(201,213,196,0) 100%);
  }
  .leaf-decor--left { left: 0; border-top-right-radius: 60% 100%; }
  .leaf-decor--right { right: 0; border-top-left-radius: 60% 100%; }

  .brand { position: relative; margin-top: 44px; display: flex; flex-direction: column; align-items: center; }
  .brand__dot { width: 26px; height: 26px; border-radius: 50%; background: var(--logo-pink); margin-bottom: 10px; }
  .brand__name { font-weight: 700; font-size: 14px; line-height: 1.15; color: var(--ink-green); letter-spacing: .5px; }

  .practice-name { position: relative; font-weight: 700; font-size: 22px; line-height: 1.05; }

  .call__label { position: relative; font-weight: 700; font-size: 15px; color: var(--violet); }
  .call__phone { position: relative; font-family: "Oswald", sans-serif; font-weight: 500; font-size: 25px; line-height: 1.15; color: var(--ink-green); }
  .call__web {
    position: relative; margin-top: 2px; padding: 2px 6px; border-radius: 8px;
    background: var(--sage); color: #fff;
    font-family: "Roboto Condensed", sans-serif; font-weight: 700; font-size: 10px;
  }

  .service { position: relative; font-weight: 800; text-transform: uppercase; line-height: 1; }
  .service__main { font-size: 24px; display: block; }
  .service__sub { font-size: 13px; font-weight: 700; display: block; margin-top: 2px; }
</style>
</head>
<body>

  <!-- Top arch row -->
  <section class="panel panel--arch-left" style="left:522px; top:24px; height:151px;">
    <div class="wave-decor" role="img" aria-label="Soft white wave ornament"></div>
    <div class="leaf-decor leaf-decor--left" role="img" aria-label="Sage leaf outline ornament"></div>
    <div class="brand">
      <span class="brand__dot"></span>
      <span class="brand__name">Fernbrook<br>Health &amp; Wellness</span>
    </div>
  </section>
  <section class="panel panel--arch-right" style="left:682px; top:24px; height:151px;">
    <div class="wave-decor wave-decor--left" role="img" aria-label="Soft white wave ornament"></div>
    <div class="leaf-decor leaf-decor--right" role="img" aria-label="Sage leaf outline ornament"></div>
    <div class="brand">
      <span class="brand__dot"></span>
      <span class="brand__name">Fernbrook<br>Health &amp; Wellness</span>
    </div>
  </section>

  <!-- Middle row -->
  <section class="panel" style="left:365px; top:182px;">
    <div class="wave-decor" role="img" aria-label="Soft white wave ornament"></div>
    <div class="leaf-decor leaf-decor--left" role="img" aria-label="Sage leaf outline ornament"></div>
    <p class="call__label">Call Today</p>
    <p class="call__phone">318-627-5194</p>
    <p class="call__web">fernbrookcare-example.com</p>
  </section>
  <section class="panel" style="left:522px; top:182px;">
    <div class="wave-decor wave-decor--left" role="img" aria-label="Soft white wave ornament"></div>
    <div class="leaf-decor leaf-decor--right" role="img" aria-label="Sage leaf outline ornament"></div>
    <p class="practice-name">Fernbrook<br>Health and<br>Wellness</p>
  </section>
  <section class="panel" style="left:682px; top:182px;">
    <div class="wave-decor wave-decor--left" role="img" aria-label="Soft white wave ornament"></div>
    <div class="leaf-decor leaf-decor--right" role="img" aria-label="Sage leaf outline ornament"></div>
    <p class="practice-name">Fernbrook<br>Health and<br>Wellness</p>
  </section>
  <section class="panel" style="left:843px; top:182px;">
    <div class="wave-decor" role="img" aria-label="Soft white wave ornament"></div>
    <div class="leaf-decor leaf-decor--left" role="img" aria-label="Sage leaf outline ornament"></div>
    <p class="call__label">Call Today</p>
    <p class="call__phone">318-627-5194</p>
    <p class="call__web">fernbrookcare-example.com</p>
  </section>

  <!-- Bottom row -->
  <section class="panel" style="left:208px; top:340px;">
    <div class="wave-decor" role="img" aria-label="Soft white wave ornament"></div>
    <div class="leaf-decor leaf-decor--left" role="img" aria-label="Sage leaf outline ornament"></div>
    <p class="service"><span class="service__main">Holistic<br>Health</span></p>
  </section>
  <section class="panel" style="left:365px; top:340px;">
    <div class="wave-decor" role="img" aria-label="Soft white wave ornament"></div>
    <div class="leaf-decor leaf-decor--left" role="img" aria-label="Sage leaf outline ornament"></div>
    <p class="service"><span class="service__main">Medical</span><span class="service__sub">Acupuncture</span></p>
  </section>
  <section class="panel" style="left:522px; top:340px;">
    <div class="wave-decor wave-decor--left" role="img" aria-label="Soft white wave ornament"></div>
    <div class="leaf-decor leaf-decor--right" role="img" aria-label="Sage leaf outline ornament"></div>
    <p class="service"><span class="service__main" style="font-size:22px;">IV Vitamin<br>Therapy</span></p>
  </section>
  <section class="panel" style="left:682px; top:340px;">
    <div class="wave-decor" role="img" aria-label="Soft white wave ornament"></div>
    <div class="leaf-decor leaf-decor--left" role="img" aria-label="Sage leaf outline ornament"></div>
    <p class="service"><span class="service__main">Direct</span><span class="service__sub">Primary Care</span></p>
  </section>
  <section class="panel" style="left:843px; top:340px;">
    <div class="wave-decor" role="img" aria-label="Soft white wave ornament"></div>
    <div class="leaf-decor leaf-decor--left" role="img" aria-label="Sage leaf outline ornament"></div>
    <p class="service"><span class="service__main">Medical</span><span class="service__sub">Acupuncture</span></p>
  </section>

</body>
</html>
```